Tarjetas de visita para empresa de aluminio

Empresa con mas de 40 años vendiendo perfiles de aluminio.
Somos fábrica y almacén, queremos renovar la tarjeta de presentación de nuestros comerciales dando una imgen innovadora y tecnógica mezclado con la calidez del respeto al medio ambiente.
Añado el logo de la empresa y actual cara trasera de la tarjeta de visita, el logo es el simbolo WM y la marca TRAVENIC EXTRUSION, la frase 2extrusion y lacado de aluminio" debe cambiarse por "Diseño, extrusión, lacado, anodizado y mecanizado de precisión de aluminio" o en su defecto incluir todos esos servicios que hacemos o una frase mas pegadiza.

We are an aluminium factory, we produce and stock profiles of aluminium.
we want to renew visit card of our sellers, we are looking for something that show innovation, tecnology and environment respect.
Upload our actual logo and back of visit card, logo WM and brand TRAVENIC EXTRUSION must be keept.
Text "Extrusion y lacado de aluminio" must be changed for "Diseño, extrusion, lacado, anodizado y mecanizado de precisión de aluminio" or something like that

```html
<!DOCTYPE html>
<html lang="es">
<head>
<meta charset="utf-8">
<title>Travenic Extrusion – Tarjetas de visita</title>
<link rel="stylesheet" href="https://fonts.googleapis.com/css2?family=Michroma&family=Open+Sans:wght@400;600;700&display=swap">
<style>
  :root{
    --page:#e8ebef;
    --navy:#0c2340;
    --blue:#1a63d8;
    --blue-soft:#e4ecfa;
    --white:#ffffff;
    --ink:#2a2f38;
    --muted:#c9d3e2;
  }
  *{box-sizing:border-box;margin:0;padding:0}
  html,body{width:1200px;height:2311px;overflow:hidden;background:var(--page)}
  .canvas{position:relative;width:1200px;height:2311px}
  .card{position:absolute;left:150px;width:900px;height:540px;overflow:hidden}
  .card--front{top:460px;background:var(--navy);display:flex;flex-direction:column;align-items:center;justify-content:center}
  .card--back{top:1260px;background:var(--white)}

  .mark-circle{width:150px;height:150px;border-radius:50%;border:8px solid var(--blue);margin-bottom:34px}
  .brand-name{font-family:"Michroma",sans-serif;color:var(--white);font-size:40px;letter-spacing:3px;white-space:nowrap}
  .brand-tagline{font-family:"Michroma",sans-serif;color:var(--muted);font-size:14px;letter-spacing:3px;line-height:1.7;margin-top:16px;text-align:center}

  .back-watermark{position:absolute;right:-90px;top:150px;width:380px;height:380px;border-radius:50%;border:34px solid var(--blue-soft)}
  .back-logo{position:absolute;left:56px;top:36px;display:flex;flex-direction:column;align-items:center}
  .back-logo .mark-circle{width:72px;height:72px;border-width:5px;margin-bottom:12px}
  .back-logo .brand-name{color:var(--blue);font-size:21px;letter-spacing:2px}
  .back-logo .brand-tagline{color:var(--blue);font-size:7.5px;letter-spacing:1.2px;line-height:1.6;margin-top:6px}

  .person{position:absolute;left:56px;width:370px;top:232px;text-align:right;font-family:"Open Sans",sans-serif}
  .person-name{color:var(--blue);font-weight:700;font-size:37px;line-height:1.3}
  .person-role{color:var(--ink);font-size:16px;margin-top:6px}

  .contacts{position:absolute;left:535px;top:228px;font-family:"Open Sans",sans-serif;color:var(--ink);font-size:15px;font-weight:600}
  .contact-row{display:flex;align-items:flex-start;gap:22px;margin-bottom:26px}
  .contact-row svg{width:24px;height:24px;flex:none;fill:var(--ink)}
  .contact-row p{line-height:1.45}

  .address-band{position:absolute;left:0;bottom:0;width:100%;height:66px;background:var(--blue);display:flex;align-items:center;gap:16px;padding-left:40px;font-family:"Open Sans",sans-serif;color:var(--white);font-weight:600;font-size:15px}
  .address-band svg{width:26px;height:26px;fill:var(--white)}
</style>
</head>
<body>
<main class="canvas">
  <section class="card card--front">
    <div class="mark-circle"></div>
    <h1 class="brand-name">TRAVENIC EXTRUSION</h1>
    <p class="brand-tagline">DISEÑO, EXTRUSIÓN, LACADO, ANODIZADO<br>Y MECANIZADO DE PRECISIÓN DE ALUMINIO</p>
  </section>

  <section class="card card--back">
    <div class="back-watermark"></div>
    <div class="back-logo">
      <div class="mark-circle"></div>
      <h2 class="brand-name">TRAVENIC EXTRUSION</h2>
      <p class="brand-tagline">DISEÑO, EXTRUSIÓN, LACADO, ANODIZADO<br>Y MECANIZADO DE PRECISIÓN DE ALUMINIO</p>
    </div>

    <div class="person">
      <p class="person-name">MARCOS LINO<br>PRIETO</p>
      <p class="person-role">COMMERCIAL</p>
    </div>

    <div class="contacts">
      <div class="contact-row">
        <svg viewBox="0 0 24 24"><path d="M6.6 10.8a15.1 15.1 0 0 0 6.6 6.6l2.2-2.2a1 1 0 0 1 1-.25 11.4 11.4 0 0 0 3.6.57 1 1 0 0 1 1 1V20a1 1 0 0 1-1 1A17 17 0 0 1 3 4a1 1 0 0 1 1-1h3.5a1 1 0 0 1 1 1c0 1.25.2 2.45.57 3.570a1 1 0 0 1-.25 1z"/></svg>
        <p>(Movil) 611 24 58 30<br>(Telf) 955 41 27 06<br>(Fax) 955 41 27 07</p>
      </div>
      <div class="contact-row">
        <svg viewBox="0 0 24 24"><path d="M2 5h20v14H2z M4 7v.4l8 5.2 8-5.2V7z" fill-rule="evenodd"/></svg>
        <p>marcoslino@travenicext.com</p>
      </div>
      <div class="contact-row">
        <svg viewBox="0 0 24 24"><path d="M12 2a10 10 0 1 0 0 20 10 10 0 0 0 0-20zm6.9 6h-3a15.7 15.7 0 0 0-1.4-3.6A8 8 0 0 1 18.9 8zM12 4c.8 1.2 1.5 2.5 1.9 4h-3.8c.4-1.5 1.1-2.8 1.9-4zM4.3 14a8 8 0 0 1 0-4h3.4a16 16 0 0 0 0 4zm.8 2h3a15.7 15.7 0 0 0 1.4 3.6A8 8 0 0 1 5.1 16zm3-8h-3a8 8 0 0 1 4.4-3.6A15.7 15.7 0 0 0 8.1 8zM12 20c-.8-1.2-1.5-2.5-1.9-4h3.8c-.4 1.5-1.1 2.8-1.9 4zm2.3-6H9.7a14 14 0 0 1 0-4h4.6a14 14 0 0 1 0 4zm.2 5.6a15.7 15.7 0 0 0 1.4-3.6h3a8 8 0 0 1-4.4 3.6zm1.8-5.6a16 16 0 0 0 0-4h3.4a8 8 0 0 1 0 4z"/></svg>
        <p>www.travenicext.com</p>
      </div>
    </div>

    <div class="address-band">
      <svg viewBox="0 0 24 24"><path d="M12 2a7 7 0 0 0-7 7c0 5.2 7 13 7 13s7-7.8 7-13a7 7 0 0 0-7-7zm0 9.5A2.5 2.5 0 1 1 12 6.5a2.5 2.5 0 0 1 0 5z"/></svg>
      <p>Pol. Ind. Norvel - C/ 4 N 22 ,41900 VILLANUEVA DEL RIO (Sevilla), Apartado de Correos 305</p>
    </div>
  </section>
</main>
</body>
</html>
```